CFO services graphic design

I own a business consulting firm called Hollins Advisory and we need a graphic for CFO services in our colours and branding. The attached file "CFO services to be put into Hollins advisory theme", shows the content for the design. The two other files show the theme and colours for the new design.

```html
<!DOCTYPE html>
<html lang="en">
<head>
<meta charset="utf-8">
<title>Chief Financial Officer Services – Hollins Advisory</title>
<link rel="stylesheet" href="https://fonts.googleapis.com/css2?family=Roboto:wght@400;700;900&display=swap">
<style>
  :root {
    --bg: #f6f7f6;
    --orange: #f39325;
    --white: #ffffff;
    --ring-grey: #e6e7e8;
    --hub-shadow: #16607f;
    --sky: #62c8f0;
    --navy: #16214a;
    --indigo: #1f3c80;
    --royal: #2a55a6;
    --cobalt: #3b6ab4;
    --steel: #337ab8;
    --cerulean: #1e9bd0;
    --azure: #27a6de;
    --icon-blue: #1fa3dc;
  }
  html, body {
    margin: 0;
    padding: 0;
    width: 1200px;
    height: 1200px;
    overflow: hidden;
    background: var(--bg);
  }
  .cfo-diagram {
    display: block;
    width: 1200px;
    height: 1200px;
    font-family: "Roboto", Arial, sans-serif;
  }
  .outline { fill: var(--orange); }
  .gap { fill: var(--white); }
  .petal { stroke: var(--white); stroke-width: 7; }
  .petal--communication { fill: var(--azure); }
  .petal--compliance { fill: var(--cerulean); }
  .petal--risk { fill: var(--steel); }
  .petal--budgeting { fill: var(--cobalt); }
  .petal--performance { fill: var(--royal); }
  .petal--investment { fill: var(--indigo); }
  .petal--capital { fill: var(--navy); }
  .petal--cost { fill: var(--sky); }
  .hub-shadow { fill: var(--hub-shadow); opacity: .55; }
  .hub-ring { fill: var(--ring-grey); }
  .hub-core { fill: var(--orange); stroke: var(--white); stroke-width: 5; }
  .hub-title { fill: var(--white); font-weight: 900; font-size: 52px; text-anchor: middle; }
  .petal-title { fill: var(--white); font-weight: 700; font-size: 26px; text-anchor: middle; }
  .petal-note { fill: var(--white); font-weight: 400; font-size: 23px; text-anchor: middle; }
  .badge-face { fill: var(--white); }
  .badge-arc-blue { fill: none; stroke: var(--icon-blue); stroke-width: 5; }
  .badge-arc-orange { fill: none; stroke: var(--orange); stroke-width: 5; }
  .glyph { fill: var(--icon-blue); }
  .glyph-line { fill: none; stroke: var(--icon-blue); stroke-width: 5; stroke-linecap: round; stroke-linejoin: round; }
  .glyph-cut { fill: var(--white); }
  .glyph-cut-line { fill: none; stroke: var(--white); stroke-width: 4; stroke-linecap: round; }
</style>
</head>
<body>
<svg class="cfo-diagram" viewBox="0 0 1500 1500" role="img" aria-label="Chief Financial Officer services: eight areas of responsibility around a central hub">
  <defs>
    <g id="badge">
      <circle class="badge-face" r="55"/>
      <path class="badge-arc-blue" d="M 0 -47 A 47 47 0 1 1 -33 33"/>
      <path class="badge-arc-orange" d="M -33 33 A 47 47 0 0 1 0 -47"/>
    </g>
    <clipPath id="compliance-area">
      <circle cx="393" cy="750" r="245"/>
    </clipPath>
  </defs>

  <!-- orange outline -->
  <g class="outline">
    <circle cx="500" cy="500" r="270"/>
    <circle cx="770" cy="395" r="265"/>
    <circle cx="1000" cy="500" r="270"/>
    <circle cx="1108" cy="760" r="265"/>
    <circle cx="1000" cy="1000" r="270"/>
    <circle cx="750" cy="1105" r="265"/>
    <circle cx="500" cy="1000" r="270"/>
    <circle cx="393" cy="750" r="265"/>
  </g>
  <g class="gap">
    <circle cx="500" cy="500" r="253"/>
    <circle cx="770" cy="395" r="248"/>
    <circle cx="1000" cy="500" r="253"/>
    <circle cx="1108" cy="760" r="248"/>
    <circle cx="1000" cy="1000" r="253"/>
    <circle cx="750" cy="1105" r="248"/>
    <circle cx="500" cy="1000" r="253"/>
    <circle cx="393" cy="750" r="248"/>
  </g>

  <!-- petals, stacked so each one overlaps its clockwise neighbour -->
  <circle class="petal petal--risk" cx="500" cy="1000" r="245"/>
  <circle class="petal petal--budgeting" cx="750" cy="1105" r="240"/>
  <circle class="petal petal--performance" cx="1000" cy="1000" r="245"/>
  <circle class="petal petal--investment" cx="1108" cy="760" r="240"/>
  <circle class="petal petal--capital" cx="1000" cy="500" r="245"/>
  <circle class="petal petal--cost" cx="770" cy="395" r="240"/>
  <circle class="petal petal--communication" cx="500" cy="500" r="245"/>
  <circle class="petal petal--compliance" cx="393" cy="750" r="240"/>
  <g clip-path="url(#compliance-area)">
    <circle class="petal petal--risk" cx="500" cy="1000" r="245"/>
  </g>

  <!-- petal labels -->
  <text class="petal-title" x="498" y="353">COMMUNICATION</text>
  <text class="petal-note" x="498" y="395">Board Of Directors,</text>
  <text class="petal-note" x="498" y="420">Creditors, Owners, Investors,</text>
  <text class="petal-note" x="498" y="445">Credit Rating Agencies</text>

  <text class="petal-title" x="828" y="258">COST</text>
  <text class="petal-title" x="828" y="288">ACCOUNTING</text>
  <text class="petal-title" x="828" y="318">&amp; COST</text>
  <text class="petal-title" x="828" y="348">MANAGEMENT</text>

  <text class="petal-title" x="1105" y="430">CAPITAL</text>
  <text class="petal-title" x="1105" y="460">STRUCTURE</text>
  <text class="petal-title" x="1105" y="490">AND THE COST</text>
  <text class="petal-title" x="1105" y="519">OF CAPITAL</text>

  <text class="petal-title" x="1160" y="798">LONG-TERM &amp;</text>
  <text class="petal-title" x="1160" y="828">SHORT-TERM</text>
  <text class="petal-title" x="1160" y="858">INVESTMENT</text>
  <text class="petal-title" x="1160" y="887">DECISIONS</text>

  <text class="petal-title" x="1002" y="1088">PERFORMANCE</text>
  <text class="petal-title" x="1002" y="1117">EVALUATION</text>

  <text class="petal-title" x="661" y="1139">BUDGETING</text>
  <text class="petal-title" x="661" y="1169">&amp; STRATEGIC</text>
  <text class="petal-title" x="661" y="1198">PLANNING</text>

  <text class="petal-title" x="400" y="963">RISK</text>
  <text class="petal-title" x="400" y="993">MANAGEMENT</text>

  <text class="petal-title" x="306" y="645">COMLIANCE</text>
  <text class="petal-note" x="316" y="681">Tax, Legal</text>
  <text class="petal-note" x="316" y="706">And Regulatory</text>

  <!-- hub -->
  <circle class="hub-shadow" cx="750" cy="750" r="285"/>
  <circle class="hub-ring" cx="750" cy="750" r="252"/>
  <circle class="hub-core" cx="752" cy="750" r="168"/>
  <text class="hub-title" x="756" y="724">CHIEF</text>
  <text class="hub-title" x="756" y="773">FINANCIAL</text>
  <text class="hub-title" x="756" y="822">OFFICER</text>

  <!-- communication badge -->
  <g transform="translate(636 517)">
    <use href="#badge"/>
    <ellipse class="glyph" cx="-6" cy="-6" rx="20" ry="15"/>
    <path class="glyph" d="M -18 4 L -22 16 L -8 8 Z"/>
    <ellipse class="glyph" cx="12" cy="8" rx="15" ry="12" stroke="#fff" stroke-width="3"/>
    <path class="glyph" d="M 20 14 L 24 24 L 12 18 Z"/>
  </g>

  <!-- cost badge -->
  <g transform="translate(840 512)">
    <use href="#badge"/>
    <rect class="glyph" x="-26" y="8" width="9" height="14"/>
    <rect class="glyph" x="-13" y="0" width="9" height="22"/>
    <rect class="glyph" x="0" y="-8" width="9" height="30"/>
    <rect class="glyph" x="13" y="-16" width="9" height="38"/>
    <path class="glyph-line" d="M -28 -2 L -8 -14 L 4 -8 L 20 -26"/>
    <path class="glyph" d="M 12 -28 L 26 -32 L 24 -18 Z"/>
  </g>

  <!-- capital badge -->
  <g transform="translate(978 636)">
    <use href="#badge"/>
    <circle class="glyph" r="27"/>
    <text x="0" y="12" fill="#fff" font-weight="900" font-size="36" text-anchor="middle">$</text>
  </g>

  <!-- investment badge -->
  <g transform="translate(988 828)">
    <use href="#badge"/>
    <rect class="glyph-line" x="-26" y="-6" width="16" height="12" rx="6"/>
    <rect class="glyph-line" x="6" y="-22" width="18" height="12" rx="6"/>
    <rect class="glyph-line" x="6" y="12" width="18" height="12" rx="6"/>
    <path class="glyph-line" d="M -10 0 L -2 0 M -2 -16 L -2 18 M -2 -16 L 6 -16 M -2 18 L 6 18"/>
  </g>

  <!-- performance badge -->
  <g transform="translate(858 975)">
    <use href="#badge"/>
    <circle class="glyph-line" cx="-6" cy="-6" r="18"/>
    <path class="glyph-line" d="M 7 7 L 24 24" stroke-width="8"/>
  </g>

  <!-- budgeting badge -->
  <g transform="translate(640 980)">
    <use href="#badge"/>
    <rect class="glyph" x="-20" y="-26" width="22" height="52"/>
    <path class="glyph" d="M 6 -18 L 18 -26 L 24 -20 L 24 26 L 6 26 Z"/>
    <rect class="glyph-cut" x="-15" y="-4" width="5" height="5"/>
    <rect class="glyph-cut" x="-6" y="-4" width="5" height="5"/>
    <rect class="glyph-cut" x="-15" y="5" width="5" height="5"/>
    <rect class="glyph-cut" x="-6" y="5" width="5" height="5"/>
    <rect class="glyph-cut" x="-15" y="14" width="5" height="5"/>
    <rect class="glyph-cut" x="-6" y="14" width="5" height="5"/>
  </g>

  <!-- risk badge -->
  <g transform="translate(518 858)">
    <use href="#badge"/>
    <path class="glyph" d="M 0 -28 L 28 22 L -28 22 Z" stroke="#1fa3dc" stroke-width="6" stroke-linejoin="round"/>
    <path class="glyph-cut-line" d="M 0 -10 L 0 6" stroke-width="6"/>
    <circle class="glyph-cut" cx="0" cy="15" r="3.5"/>
  </g>

  <!-- compliance badge -->
  <g transform="translate(510 660)">
    <use href="#badge"/>
    <rect class="glyph-line" x="-22" y="-26" width="36" height="48" stroke-width="4"/>
    <path class="glyph-line" d="M -15 -16 L 7 -16 M -15 -8 L 7 -8 M -15 0 L 7 0 M -15 8 L 0 8" stroke-width="3.5"/>
    <path class="glyph-line" d="M 2 14 L 10 22 L 26 4" stroke-width="5"/>
  </g>
</svg>
</body>
</html>
```